Web Design Project

[Website design criteria]

Develop a unique and 'different' legal website that focuses on collaborative divorce. I have a successful adversarial divorce practice and am branching out. My current website is "www.theseparationpal.net" and "http://www.brantoverlegal.net/Partners.html" for the law firm.

As an aside, collaborative divorce is a mechanism by which the parties with their attorneys attempt to facilitate settlement vs. an adversarial proceeding. I like standing out (but respectful to the process (divorce) - so dare to be different)

The website name is: apeacefulparting.net

Headline samples: (utilize or become inspired by the following or your own)

"Avoid the uncertain outcome of court and achieve a fair settlement."
"Fulfill your goals without contested litigation."

(areas of specialization)
Specializing in:
Alternative dispute resolution
Collaborative divorce,
Divorce mediation
Lawyer assisted divorce
One attorney divorce

Benefits:
Divorce without the fight
Fairly settle your own case
Avoid litigation
Save money
Save time
Reduce stress and anxiety

Disadvantages:
When parties are committed to settlement and litigation is not an option, creativity and flexibility in problem solving becomes the norm. However, if cooperation and flexibility is not possible, a more traditional, adversiaral divorce is appropriate.

Target Market(s)

Michigan residents considering divorce

I want the website to have a different feel than my current websites. Specifically, I want to compete against myself. So, the picture of me is a no etc.

Here are some competing sites that I liked.

http://gentlesplitpath.net/

Here are some other sites I like.

http://worthelandpruitt.adgrowthhub.net/?utm_source=Adgrowthhub&utm_medium=PPC&utm_campaign=Familylaw

Industry/Entity Type

Attorney

Requirements
Must have
• Call to action window:
The window should include Name, email, phone, question. (See: www.theseparationpal.net)

Phone number: 866-TEAM BEST
248-555-0172

Room for headlines (as I like to blog, using wordpress)
Nice to have
• Creative and Different are a plus. Think outside the "box".

Should not have
• Traditional website layouts. Library books, scales of justice etc.

```html
<!DOCTYPE html>
<html lang="en">
<head>
<meta charset="utf-8">
<title>apeacefulparting.net</title>
<link rel="stylesheet" href="https://fonts.googleapis.com/css2?family=Arimo:wght@400;700&display=swap">
<style>
:root{
  --orange:#ff8420;
  --orange-light:#ffb266;
  --nav-bg:#f1f1f1;
  --grey-bar:#9a9a9a;
  --text:#555;
  --text-dark:#222;
  --form-head:#3a3a3a;
  --tick:#44c21a;
}
*{box-sizing:border-box;margin:0;padding:0}
html,body{width:1200px;height:886px;overflow:hidden;background:#fff;font-family:"Arimo",Arial,sans-serif;color:var(--text)}
.page{position:relative;width:1200px;height:886px}
.topstrip{position:absolute;left:0;top:0;width:1200px;height:6px;background:var(--orange-light)}
.header{position:absolute;left:0;top:6px;width:1200px;height:79px;background:linear-gradient(#ff8a24,#ff7d16)}
.brand{position:absolute;left:186px;top:22px;font-size:32px;color:#fff;letter-spacing:.5px}
.call{position:absolute;left:826px;top:18px;display:flex;align-items:center;gap:6px}
.call-icon{width:47px;height:47px}
.call-numbers{color:#fff;font-weight:700;font-size:16px;line-height:18px;text-align:right}
.nav{position:absolute;left:0;top:85px;width:1200px;height:42px;background:linear-gradient(#fafafa,#ebebeb);border-bottom:1px solid #e2e2e2}
.nav ul{list-style:none;position:absolute;left:188px;top:0;display:flex;height:42px}
.nav li{font-size:12px;font-weight:700;color:#666;line-height:42px;padding:0 13px;position:relative}
.nav li+li::before{content:"";position:absolute;left:0;top:10px;height:22px;border-left:1px solid #d6d6d6}
.nav li.active{background:var(--orange);color:#fff;width:87px;text-align:center;padding:0}
.nav li.active::after{content:"";position:absolute;left:38px;bottom:-6px;border:6px solid transparent;border-top-color:var(--orange);border-bottom:0}
.nav li.active+li::before{display:none}
.nav li.first{margin-left:14px}
.hero{position:absolute;left:0;top:127px;width:1200px;height:237px;background:linear-gradient(#ededed,#fff)}
.hero-photo{position:absolute;left:507px;top:156px;width:279px;height:203px;background:radial-gradient(ellipse at 60% 45%,#e9c9ad 0%,#dedede 50%,rgba(240,240,240,0) 78%)}
.headline{position:absolute;z-index:2;left:188px;top:170px;width:400px;font-size:25px;line-height:30px;color:var(--text-dark);font-weight:400;white-space:nowrap}
.learn{position:absolute;left:188px;top:292px;width:87px;height:23px;background:var(--orange);border-radius:3px;color:#fff;font-size:12px;font-weight:700;line-height:23px;padding-left:7px}
.learn::after{content:"›";position:absolute;right:6px;top:0}
.form{position:absolute;left:788px;top:128px;width:225px;height:231px;background:linear-gradient(#f7f7f7,#ececec)}
.form-head{height:44px;background:var(--form-head);color:#fff;padding:7px 12px}
.form-head h2{font-size:15px;font-weight:700;line-height:16px}
.form-head p{font-size:9.5px;font-weight:700}
.field{position:absolute;left:9px;font-size:11px;color:#666;display:flex;align-items:center}
.field span{width:62px}
.field i{font-style:normal;width:11px}
.field b{display:block;width:135px;height:16px;background:#fff;border:1px solid #ddd}
.question-box{position:absolute;left:9px;top:131px;width:207px;height:44px;background:#fff;border:1px solid #ddd}
.submit{position:absolute;left:9px;top:184px;width:207px;height:28px;border-radius:4px;background:linear-gradient(#ff8a2e,#f45c0c);color:#fff;font-weight:700;font-size:14px;text-align:center;line-height:28px}
.section-bar{position:absolute;left:186px;top:367px;width:828px;height:30px;background:var(--grey-bar);border-top:4px solid #b8b8b8;color:#fff;font-size:17px;font-weight:700;padding:2px 8px}
.intro{position:absolute;left:194px;top:415px;width:812px;font-size:10px;line-height:12.3px}
.intro p+p{margin-top:11px}
.benefits-bar{position:absolute;left:186px;top:507px;width:276px;height:27px;background:var(--grey-bar);border-top:3px solid #b8b8b8;color:#fff;font-size:16px;font-weight:700;padding:1px 7px}
.benefits{position:absolute;left:192px;top:552px;list-style:none;font-size:11px;color:#666}
.benefits li{height:17.6px;display:flex;align-items:center;gap:9px}
.benefits svg{width:12px;height:10px}
.blogs{position:absolute;left:470px;top:507px;width:543px;height:182px;background:linear-gradient(90deg,#ececec,#fafafa 60%,#fff)}
.blogs h2{position:absolute;left:13px;top:5px;font-size:18px;color:var(--text-dark);font-weight:700}
.post{position:absolute;left:13px;width:520px}
.post h3{font-size:12px;color:#666;font-weight:700}
.post p{width:508px;font-size:10px;line-height:12px;margin-top:3px;text-align:justify}
.post.one{top:37px;padding-bottom:9px;border-bottom:1px dashed #ccc}
.post.two{top:97px}
.view-all{position:absolute;right:14px;top:152px;font-size:11px;color:var(--text-dark)}
.view-all::after{content:" ›";font-weight:700}
.footer-line{position:absolute;left:186px;top:739px;width:828px;border-top:1px solid #e4e4e4}
.address{position:absolute;left:186px;top:762px;font-size:12px;color:var(--text-dark)}
.copyright{position:absolute;right:194px;top:762px;font-size:10px;color:#666}
.footer-links{position:absolute;left:186px;top:780px;display:flex;font-size:10px;color:#777;list-style:none}
.footer-links li+li::before{content:"";display:inline-block;width:3px;height:3px;border:1px solid #555;border-radius:50%;margin:0 3px 1px}
</style>
</head>
<body>
<div class="page">
  <div class="topstrip"></div>
  <header class="header">
    <div class="brand">apeacefulparting.net</div>
    <div class="call">
      <svg class="call-icon" viewBox="0 0 48 48" aria-hidden="true">
        <circle cx="24" cy="24" r="22" fill="#222" stroke="#fff" stroke-width="3"/>
        <path d="M17 13c2-1 3 0 4 2l1 4c0 1-1 2-2 3 1 3 3 5 6 6 1-1 2-2 3-2l4 1c2 1 3 2 2 4-1 2-3 4-6 3-8-2-13-7-15-15-1-3 1-5 3-6z" fill="#fff"/>
      </svg>
      <div class="call-numbers">866-TEAM BEST<br>248-555-0172</div>
    </div>
  </header>

  <nav class="nav">
    <ul>
      <li class="active">Home</li>
      <li class="first">Choosing an Attorney</li>
      <li>Planning For Divorce</li>
      <li>Alternatives</li>
      <li>The Formal Process</li>
      <li>Property Division</li>
      <li>Alimony</li>
    </ul>
  </nav>

  <section class="hero"></section>
  <div class="hero-photo" role="img" aria-label="Photo of a smiling father helping his son with homework at a table"></div>
  <h1 class="headline">Avoid the uncertain outcome of<br>court and achieve a fair<br>settlement.</h1>
  <div class="learn">Learn More</div>

  <aside class="form">
    <div class="form-head">
      <h2>Confidential Question?</h2>
      <p>Please fill out the simple form below</p>
    </div>
    <div class="field" style="top:60px"><span>Name</span><i>:</i><b></b></div>
    <div class="field" style="top:80px"><span>Email</span><i>:</i><b></b></div>
    <div class="field" style="top:100px"><span>Phone</span><i>:</i><b></b></div>
    <div class="field" style="top:118px"><span>Question</span><i>:</i></div>
    <div class="question-box"></div>
    <div class="submit">Get Answers Now!</div>
  </aside>

  <h2 class="section-bar">We have the answers you need</h2>
  <div class="intro">
    <p>Welcome, we are ready to help. The Brantover Law Firm is a leading Michigan divorce law firm, dedicated to fulfilling your goals by solving complex problems.</p>
    <p>Change is rarely easy, sometimes complicated and often emotional. Our experienced family law lawyers and support group utilize a team approach to focus on solutions. We apply Michigan law and specialize in helping you focus on your goals, protect your property interests, manage your custody and support interest, and keep you happy. Our commitment is to solve problems at an affordable cost. We love to settle cases, but are not afraid to fight.</p>
  </div>

  <h2 class="benefits-bar">Benefits</h2>
  <ul class="benefits">
    <li><svg viewBox="0 0 12 10"><path d="M1 5l3.5 3.5L11 1.5" fill="none" stroke="#44c21a" stroke-width="2.4"/></svg>Divorce without the fight</li>
    <li><svg viewBox="0 0 12 10"><path d="M1 5l3.5 3.5L11 1.5" fill="none" stroke="#44c21a" stroke-width="2.4"/></svg>Fairly settle your own case</li>
    <li><svg viewBox="0 0 12 10"><path d="M1 5l3.5 3.5L11 1.5" fill="none" stroke="#44c21a" stroke-width="2.4"/></svg>Avoid litigation</li>
    <li><svg viewBox="0 0 12 10"><path d="M1 5l3.5 3.5L11 1.5" fill="none" stroke="#44c21a" stroke-width="2.4"/></svg>Save money</li>
    <li><svg viewBox="0 0 12 10"><path d="M1 5l3.5 3.5L11 1.5" fill="none" stroke="#44c21a" stroke-width="2.4"/></svg>Save time</li>
    <li><svg viewBox="0 0 12 10"><path d="M1 5l3.5 3.5L11 1.5" fill="none" stroke="#44c21a" stroke-width="2.4"/></svg>Reduce stress and anxiety</li>
  </ul>

  <section class="blogs">
    <h2>Recent Blogs</h2>
    <article class="post one">
      <h3>If you or a loved one is struggling in their situation, take a look around our site</h3>
      <p>Night Desk uncovered several such documents in the fall, including some instructing FBI counterterrorism agents.</p>
    </article>
    <article class="post two">
      <h3>If you or a loved one is struggling in their situation</h3>
      <p>Night Desk uncovered several such documents in the fall, including some instructing FBI counterterrorism agents.</p>
    </article>
    <div class="view-all">View All Blogs</div>
  </section>

  <div class="footer-line"></div>
  <div class="address">220 w. Elm Street, Royal Oak, mi 48067 248.555.0172 - Email:mark@brantoverlegal.net</div>
  <div class="copyright">Copyright © 2012</div>
  <ul class="footer-links">
    <li>Choosing an Attorney</li>
    <li>Planning For Divorce</li>
    <li>Alternatives</li>
    <li>The Formal Process</li>
    <li>Property Division</li>
    <li>Alimony</li>
  </ul>
</div>
</body>
</html>
```